VMR business card

Need a business card for a company that provides instructional design and elearning development services. The website is here: http://vantmoro.studio/

I'm attaching a current logo, as well as the old business card design. While I like to keep it clean, the old design is too simplistic for my liking. The only idea I want to reuse from the old design is placing industry jargon on the back of the card, just need a better way to present it. But if you have other ideas for the back--feel free to experiment.

Please use the colors complementary to the color we have on the website. Thank you!

```html
<!DOCTYPE html>
<html lang="en">
<head>
<meta charset="utf-8">
<title>VMR business card</title>
<link rel="stylesheet" href="https://fonts.googleapis.com/css2?family=Montserrat:wght@600;700&family=Arimo:wght@400;700&display=swap">
<style>
  :root {
    --teal: #1a9d95;
    --gold: #d6c79c;
    --ink: #3d3d3d;
    --rule: #6a6a6a;
    --paper: #ffffff;
    --ground: #e9eaec;
  }
  * { box-sizing: border-box; margin: 0; padding: 0; }
  html, body { width: 1200px; height: 900px; overflow: hidden; }
  body {
    background: var(--ground);
    font-family: "Arimo", Arial, sans-serif;
    color: var(--ink);
    position: relative;
  }
  .card {
    position: absolute;
    left: 290px;
    width: 620px;
    height: 380px;
    background: var(--paper);
    border-radius: 26px;
    box-shadow: 0 6px 22px rgba(0,0,0,.12);
    overflow: hidden;
  }
  .card--back { top: 45px; }
  .card--front { top: 475px; }

  /* Back: question beside a set of service tags */
  .services-ask {
    position: absolute;
    left: 48px; top: 50%;
    transform: translateY(-50%);
    width: 190px;
    font-family: "Montserrat", Arial, sans-serif;
    font-weight: 700;
    font-size: 34px;
    line-height: 40px;
    color: var(--teal);
    text-transform: uppercase;
  }
  .services-divider {
    position: absolute;
    left: 250px; top: 60px;
    width: 2px; height: 260px;
    background: var(--gold);
  }
  .services {
    position: absolute;
    left: 276px; top: 50%;
    transform: translateY(-50%);
    width: 310px;
    list-style: none;
    display: flex; flex-wrap: wrap; gap: 9px 8px;
  }
  .services li {
    border: 1.5px solid var(--gold);
    border-radius: 16px;
    padding: 6px 11px;
    font-size: 13px;
    font-weight: 700;
    letter-spacing: 1px;
    text-transform: uppercase;
    white-space: nowrap;
    color: var(--ink);
  }

  /* Front */
  .brand {
    position: absolute;
    left: 150px; top: 140px;
    display: flex; align-items: center; gap: 14px;
  }
  .brand__dot { width: 34px; height: 34px; border-radius: 50%; background: var(--teal); }
  .brand__name {
    font-family: "Montserrat", Arial, sans-serif;
    font-weight: 700;
    font-size: 42px;
    color: var(--teal);
  }
  .brand-rule {
    position: absolute;
    left: 390px; top: 208px;
    width: 200px; height: 2px;
    background: var(--rule);
  }
  .holder {
    position: absolute;
    right: 30px; top: 218px;
    font-family: "Montserrat", Arial, sans-serif;
    font-weight: 700;
    font-size: 21px;
    color: var(--teal);
    letter-spacing: .5px;
  }
  .contact-rule {
    position: absolute;
    left: 24px; top: 282px;
    width: 330px; height: 2px;
    background: var(--rule);
  }
  .contacts {
    position: absolute;
    left: 26px; top: 294px;
    list-style: none;
  }
  .contacts li {
    display: flex; align-items: center; gap: 10px;
    font-size: 17px; font-weight: 700;
    line-height: 24px;
    color: var(--ink);
  }
  .contacts svg { width: 14px; height: 14px; flex: none; }
</style>
</head>
<body>

<section class="card card--back" aria-label="Card back">
  <p class="services-ask">How can we help?</p>
  <div class="services-divider"></div>
  <ul class="services">
    <li>Instructional design</li>
    <li>Mobile learning</li>
    <li>SCORM</li>
    <li>LMS</li>
    <li>xAPI</li>
    <li>HTML5</li>
    <li>MOOCs</li>
    <li>Adult learning theory</li>
    <li>Gamification</li>
    <li>Blended learning</li>
    <li>Classroom</li>
  </ul>
</section>

<section class="card card--front" aria-label="Card front">
  <div class="brand">
    <span class="brand__dot"></span>
    <span class="brand__name">Vantmoro Studio</span>
  </div>
  <div class="brand-rule"></div>
  <p class="holder">DORIAN KELBRECHT</p>
  <div class="contact-rule"></div>
  <ul class="contacts">
    <li>
      <svg viewBox="0 0 16 16" aria-hidden="true"><path fill="var(--teal)" d="M3 1l3 3-2 2c1 2 3 4 5 5l2-2 3 3-2 3C7 15 1 9 1 3z"/></svg>
      555-014-2278
    </li>
    <li>
      <svg viewBox="0 0 16 16" aria-hidden="true"><g fill="none" stroke="var(--teal)" stroke-width="1.5"><circle cx="8" cy="8" r="6.5"/><ellipse cx="8" cy="8" rx="3" ry="6.5"/><path d="M1.5 8h13"/></g></svg>
      www.vantmoro.studio
    </li>
    <li>
      <svg viewBox="0 0 16 16" aria-hidden="true"><g fill="none" stroke="var(--teal)" stroke-width="1.5"><rect x="1.5" y="3.5" width="13" height="9"/><path d="M1.5 3.5l6.5 5 6.5-5"/></g></svg>
      dkelbrecht@vantmoro.studio
    </li>
  </ul>
</section>

</body>
</html>
```